Creative Businesss Card desgin!

Create a business card for our business Gleam window cleaning!
We are open to creative ideas as long as it maintains a professional image.

Target Market(s)

Small Commercial window cleaning clients including car dealerships, strata manager, cafe

Industry/Entity Type

Window Cleaning

Contact Information for Business Card

Daniel Prescott
General Manager
Gleam Window Cleaning

daniel@gleamservices.com.au
pane-care-southbank.com.au
Ph: 1800 GET GLEAM
Mob: 0437 582 061

Colors
fbed22
0392cd

Requirements
Should not have
• Stock window cleaning/ squeegee graphics

```html
<!DOCTYPE html>
<html lang="en">
<head>
<meta charset="utf-8">
<title>Gleam Window Cleaning – Business Card</title>
<link href="https://fonts.googleapis.com/css2?family=Arimo:wght@400;700&display=swap" rel="stylesheet">
<style>
  :root {
    --bg: #2b2b2b;
    --card-blue: #0d5d92;
    --card-blue-deep: #0a4c79;
    --yellow: #fbed22;
    --ink: #0a3f66;
    --text-light: #e8eef3;
  }
  * { box-sizing: border-box; margin: 0; padding: 0; }
  html, body { width: 1200px; height: 997px; overflow: hidden; }
  body {
    background: var(--bg);
    font-family: "Arimo", Arial, sans-serif;
    position: relative;
  }
  .card {
    position: absolute;
    width: 540px;
    height: 310px;
    border-radius: 16px;
    overflow: hidden;
    background: linear-gradient(160deg, var(--card-blue) 0%, var(--card-blue-deep) 100%);
    box-shadow: 0 14px 30px rgba(0,0,0,.45);
  }
  .card-front { left: 70px; top: 130px; }
  .card-back { left: 590px; top: 480px; }

  .wordmark {
    position: absolute;
    color: var(--yellow);
    font-weight: 700;
    line-height: 1;
  }
  .wordmark .name { display: block; letter-spacing: 2px; }
  .wordmark .sub { display: block; letter-spacing: 1px; }

  .card-front .wordmark { left: 60px; top: 90px; }
  .card-front .wordmark .name { font-size: 84px; }
  .card-front .wordmark .sub { font-size: 27px; margin-top: 6px; }

  .rule {
    position: absolute;
    height: 2px;
    background: var(--yellow);
  }
  .band {
    position: absolute;
    left: 0; right: 0; bottom: 0;
    background: var(--yellow);
    color: var(--ink);
    display: flex;
    align-items: center;
  }
  .card-front .rule { left: 0; right: 0; bottom: 44px; }
  .card-front .band { height: 36px; justify-content: flex-end; padding-right: 22px; font-size: 12px; }
  .card-front .band span + span { margin-left: 14px; }

  .card-back .wordmark { left: 30px; top: 30px; }
  .card-back .wordmark .name { font-size: 46px; }
  .card-back .wordmark .sub { font-size: 15px; margin-top: 4px; }
  .card-back .rule-top { left: 250px; right: 20px; top: 92px; }
  .card-back .rule-name { left: 210px; right: 20px; top: 160px; }

  .person { position: absolute; left: 30px; top: 140px; }
  .person .full-name { color: var(--yellow); font-weight: 700; font-size: 19px; }
  .person .role { color: var(--text-light); font-size: 13px; margin-top: 3px; }

  .contacts {
    position: absolute;
    left: 30px; top: 206px;
    list-style: none;
    color: var(--text-light);
    font-size: 14px;
  }
  .contacts li { display: flex; align-items: center; height: 20px; }
  .contacts svg { width: 14px; height: 14px; margin-right: 9px; flex: none; }

  .address {
    position: absolute;
    right: 22px; top: 222px;
    color: var(--yellow);
    font-size: 13px;
  }
  .card-back .rule-band { left: 0; right: 0; bottom: 40px; }
  .card-back .band { height: 32px; justify-content: center; font-size: 15px; font-weight: 700; }
</style>
</head>
<body>

  <section class="card card-front">
    <div class="wordmark">
      <span class="name">GLEAM</span>
      <span class="sub">WINDOW CLEANING</span>
    </div>
    <div class="rule"></div>
    <div class="band">
      <span>Pressure Cleaning</span><span>Gutter Cleaning</span><span>Graffiti Removal</span>
    </div>
  </section>

  <section class="card card-back">
    <div class="wordmark">
      <span class="name">GLEAM</span>
      <span class="sub">WINDOW CLEANING</span>
    </div>
    <div class="rule rule-top"></div>

    <div class="person">
      <p class="full-name">Daniel Prescott</p>
      <p class="role">General Manager</p>
    </div>
    <div class="rule rule-name"></div>

    <ul class="contacts">
      <li>
        <svg viewBox="0 0 14 14" aria-hidden="true"><circle cx="7" cy="7" r="7" fill="#fbed22"/><path d="M4.2 3.6l1.5-.3.8 1.8-.9.7a4.6 4.6 0 0 0 2.6 2.6l.7-.9 1.8.8-.3 1.5c-3.4.3-6.5-2.8-6.2-6.2z" fill="#0a3f66"/></svg>
        0437 582 061
      </li>
      <li>
        <svg viewBox="0 0 14 14" aria-hidden="true"><circle cx="7" cy="7" r="7" fill="#fbed22"/><path d="M4.2 3.6l1.5-.3.8 1.8-.9.7a4.6 4.6 0 0 0 2.6 2.6l.7-.9 1.8.8-.3 1.5c-3.4.3-6.5-2.8-6.2-6.2z" fill="#0a3f66"/></svg>
        1800 GET GLEAM
      </li>
      <li>
        <svg viewBox="0 0 14 14" aria-hidden="true"><circle cx="7" cy="7" r="7" fill="#fbed22"/><rect x="3.5" y="4.5" width="7" height="5" fill="none" stroke="#0a3f66" stroke-width="1"/><path d="M3.5 4.5L7 7.3l3.5-2.8" fill="none" stroke="#0a3f66" stroke-width="1"/></svg>
        daniel@gleamservices.com.au
      </li>
    </ul>

    <p class="address">1208/45 Harbour Rd Southbank VIC 3006</p>
    <div class="rule rule-band"></div>
    <div class="band">www.pane-care-southbank.com.au</div>
  </section>

</body>
</html>
```